Heron Haulage Ltd

We need an A5 size (UK size) flyer to advertise our new business which is called Heron Haulage.
Domestic and Commercial Waste Clearance Services.
Please have the question in bold "Do you have a pile of junk you need to dispose of?"
We collect all kinds of junk or rubbish from homes and businesses across Kent, Sussex and South London.
No fuss, no mess!
A low cost, hassle free alternative to skip hire.
Licensed by the Landcare Board and fully insured (this can be in small print at the bottom).
Please put the Recycle symbol somewhere.
Our tagline on our vehicle is "We Clear More, For Less!"
We'd like the flyer to be bold and eye-catching (to catch the eye of the homeowner or business owner while it's sitting on their doormat).
We need our telephone, website and email to be prominent. Maybe saying "Call today for a free quote"
Tel. 01734 580916
Email: info@heronhaulage.example
www.heronhaulage.example
Target Market(s)
Our market will be homes and small businesses around Kent, Sussex and South London.
Industry/Entity Type
Business
Font styles to use
Look and feel

```html
<!DOCTYPE html>
<html lang="en">
<head>
<meta charset="utf-8">
<title>Heron Haulage – Waste Clearance Flyer</title>
<link rel="stylesheet" href="https://fonts.googleapis.com/css2?family=Oswald:wght@500;700&display=swap">
<style>
  :root {
    --green: #1c9c48;
    --green-dark: #15823a;
    --lime: #b3d235;
    --lime-dark: #8fb02a;
    --grey: #58595b;
    --grey-dot: #8a8b8d;
    --white: #ffffff;
  }
  html, body {
    margin: 0;
    padding: 0;
    overflow: hidden;
    background: #e9e9e9;
  }
  .flyer {
    position: relative;
    width: 845px;
    height: 1200px;
    overflow: hidden;
    background: var(--green);
    font-family: "Oswald", "Arial Narrow", sans-serif;
    color: var(--white);
  }
  .backdrop {
    position: absolute;
    inset: 0;
  }
  .headline {
    position: absolute;
    right: 190px;
    top: 168px;
    margin: 0;
    text-align: right;
    font-weight: 700;
    text-transform: uppercase;
    line-height: 1.05;
    letter-spacing: 0.2px;
  }
  .headline__first {
    display: block;
    color: var(--grey);
    font-size: 45px;
  }
  .headline__second {
    display: block;
    color: var(--green);
    font-size: 45px;
  }
  .mascot {
    position: absolute;
    left: 215px;
    top: 300px;
    width: 400px;
    height: 470px;
    border-radius: 40px 40px 60px 60px;
    background: radial-gradient(ellipse at 50% 40%, var(--lime) 0%, var(--lime-dark) 100%);
  }
  .recycle-badge {
    position: absolute;
    left: 628px;
    top: 678px;
    width: 154px;
    height: 154px;
    border-radius: 50%;
    background: var(--white);
  }
  .recycle-badge__symbol {
    position: absolute;
    left: 32px;
    top: 32px;
    width: 90px;
    height: 90px;
    border-radius: 50%;
    background: radial-gradient(circle, #6fcf5a 0%, var(--green-dark) 100%);
  }
  .service {
    position: absolute;
    left: 0;
    right: 0;
    top: 836px;
    margin: 0;
    text-align: center;
    font-weight: 500;
    font-size: 23px;
    line-height: 29px;
  }
  .divider {
    position: absolute;
    left: 160px;
    width: 528px;
    top: 941px;
    border-top: 2px dotted rgba(255,255,255,0.75);
  }
  .tagline {
    position: absolute;
    left: 0;
    right: 0;
    top: 950px;
    margin: 0;
    text-align: center;
    font-weight: 500;
    font-size: 25px;
    text-transform: uppercase;
  }
  .brand-box {
    position: absolute;
    left: 37px;
    top: 1039px;
    width: 322px;
    height: 136px;
    background: var(--white);
    display: flex;
    align-items: center;
    justify-content: center;
  }
  .brand-box__name {
    color: var(--grey);
    font-weight: 700;
    font-size: 40px;
    text-transform: uppercase;
    letter-spacing: 1px;
  }
  .contact {
    position: absolute;
    left: 377px;
    top: 1050px;
    width: 430px;
  }
  .contact__call {
    margin: 0;
    font-weight: 500;
    font-size: 24px;
    line-height: 32px;
    text-transform: uppercase;
  }
  .contact__details {
    margin: 6px 0 0;
    font-weight: 500;
    font-size: 15px;
    line-height: 23px;
  }
  .contact__rule {
    margin: 8px 0 0;
    border: 0;
    border-top: 1px solid rgba(255,255,255,0.85);
  }
  .contact__licence {
    margin: 6px 0 0;
    font-weight: 500;
    font-size: 16px;
  }
</style>
</head>
<body>
<main class="flyer">
  <svg class="backdrop" width="845" height="1200" viewBox="0 0 845 1200" aria-hidden="true">
    <path d="M120 0 C 40 220, 130 560, 520 690 C 640 728, 760 738, 845 735 L845 0 Z" fill="#ffffff"/>
    <path d="M0 290 C 60 560, 260 720, 560 775" fill="none" stroke="#ffffff" stroke-width="3"/>
    <path d="M60 0 C 0 260, 120 560, 480 680" fill="none" stroke="#9a9b9d" stroke-width="4" stroke-dasharray="2 6"/>
    <path d="M520 690 C 600 712, 700 720, 845 708" fill="none" stroke="#9a9b9d" stroke-width="4" stroke-dasharray="2 6"/>
    <path d="M652 95 C 652 25, 762 15, 762 95 C 762 150, 692 165, 692 238" fill="none" stroke="#1c9c48" stroke-width="46"/>
    <circle cx="692" cy="292" r="26" fill="#58595b"/>
  </svg>

  <h1 class="headline">
    <span class="headline__first">Do you have a pile of junk</span>
    <span class="headline__second">You need to dispose of</span>
  </h1>

  <div class="mascot" role="img" aria-label="Cartoon illustration of a smiling lime-green waste bin character with a lid, waving"></div>

  <div class="recycle-badge">
    <div class="recycle-badge__symbol" role="img" aria-label="Green recycling symbol"></div>
  </div>

  <p class="service">We collect all kinds of junk or rubbish<br>from homes and businesses across<br>Kent, Sussex and South London. No fuss, no mess!</p>
  <div class="divider"></div>
  <p class="tagline">A low cost, hassle free alternative to skip hire.</p>

  <div class="brand-box">
    <span class="brand-box__name">Heron Haulage</span>
  </div>

  <section class="contact">
    <p class="contact__call">Call today for a free quote :</p>
    <p class="contact__details">Tel. 01734 580916, Email: info@heronhaulage.example<br>www.heronhaulage.example</p>
    <hr class="contact__rule">
    <p class="contact__licence">Licensed by the Landcare Board and fully insured</p>
  </section>
</main>
</body>
</html>
```